Celebrity and Entertainment News Website Needed

Entertainment is one of the favors of Life and I am seeking a standard celebrity website which will discuss in depth news of different celebrities around globe with major focus on American Entertainers. There will be different categories of news from these regions. America, Europe, Asia, Australia and Africa. My website name is coralvista. Youthful colors should be used for the theme and designs, Users should be able to comment at the bottom of each news. Glossy pictures of well know celebrities should be used. Designers can get knowledge from http://qarvetto.com

```html
<!DOCTYPE html>
<html lang="en">
<head>
<meta charset="utf-8">
<title>coralvista – Individual Category Area</title>
<link href="https://fonts.googleapis.com/css2?family=Titillium+Web:wght@600&family=Catamaran:wght@600&family=Open+Sans:wght@400;600&display=swap" rel="stylesheet">
<style>
  :root{
    --board:#523d3c;
    --board-title:#c9b3b3;
    --panel:#ffffff;
    --ink:#222222;
    --tab:#333333;
    --accent:#1a8fd1;
    --muted:#9a9a9a;
    --rule:#333333;
    --btn-border:#d8d8d8;
  }
  *{box-sizing:border-box;margin:0;padding:0}
  html,body{width:1200px;height:1200px;overflow:hidden;background:var(--board)}
  .board{position:relative;width:1200px;height:1200px}
  .board-title{
    position:absolute;left:213px;top:38px;
    font-family:"Titillium Web",sans-serif;font-weight:600;font-size:36px;
    color:var(--board-title);letter-spacing:.3px;white-space:nowrap;
  }
  .board-title .gap{display:inline-block;width:22px}
  .panel{
    position:absolute;left:86px;top:122px;width:1024px;height:1025px;
    background:var(--panel);overflow:hidden;padding:17px 35px 0;
  }
  .category + .category{margin-top:23px}
  .category-head{
    display:flex;justify-content:space-between;align-items:flex-end;
    border-bottom:2px solid var(--rule);height:28px;
  }
  .category-tab{
    background:var(--tab);color:#fff;height:26px;padding:0 11px;
    font-family:"Open Sans",sans-serif;font-weight:600;font-size:13px;
    display:flex;align-items:center;
  }
  .view-all{
    align-self:flex-start;border:1px solid var(--btn-border);
    font-family:"Open Sans",sans-serif;font-size:8px;color:#444;
    padding:5px 11px;letter-spacing:.2px;
  }
  .card-grid{
    display:grid;grid-template-columns:repeat(3,302px);column-gap:24px;
    row-gap:24px;grid-auto-rows:293px;margin-top:14px;
  }
  .card-image{position:relative;height:169px;display:flex;align-items:center;justify-content:center}
  .card-label{
    margin-top:13px;font-family:"Open Sans",sans-serif;font-size:10px;
    color:var(--accent);text-transform:uppercase;
  }
  .card-title{
    margin-top:4px;font-family:"Catamaran",sans-serif;font-weight:600;
    font-size:19.2px;line-height:25.6px;color:var(--ink);
  }
  .card-meta{
    display:flex;align-items:center;gap:4px;
    font-family:"Open Sans",sans-serif;font-size:10.4px;color:var(--muted);
  }
  .gallery-badge{width:48px;height:48px}
</style>
</head>
<body>
<div class="board">
  <h1 class="board-title">Design Idea - 1b<span class="gap"></span>[ Individual Category Area ]</h1>

  <main class="panel">
    <section class="category">
      <header class="category-head">
        <h2 class="category-tab">America</h2>
        <span class="view-all">VIEW ALL</span>
      </header>
      <div class="card-grid">
        <article class="card">
          <div class="card-image" role="img" aria-label="Photo of an actor visiting a woman in a hospital bed" style="background:linear-gradient(135deg,#3f3a33,#8d8478 45%,#c9c3ba 70%,#a39b90)"></div>
          <p class="card-label">America</p>
          <h3 class="card-title">The Marlowes Is Oozing With Jonah Kessler’s Charm, But How Does the Rest of the Movie Hold Up?</h3>
          <p class="card-meta"><svg width="9" height="9" viewBox="0 0 10 10"><circle cx="5" cy="5" r="4" fill="none" stroke="#9a9a9a" stroke-width="1.2"/><path d="M5 2.6V5h2" fill="none" stroke="#9a9a9a" stroke-width="1.2"/></svg>10 months ago</p>
        </article>
        <article class="card">
          <div class="card-image" role="img" aria-label="Photo of a smiling actor at a convention backdrop" style="background:linear-gradient(90deg,#d9d9d9,#efefef 55%,#c9c28a 85%,#e4e4e4)"></div>
          <p class="card-label">America</p>
          <h3 class="card-title">Tim Harrowgate’s Snapwall Account Gets Hacked</h3>
          <p class="card-meta"><svg width="9" height="9" viewBox="0 0 10 10"><circle cx="5" cy="5" r="4" fill="none" stroke="#9a9a9a" stroke-width="1.2"/><path d="M5 2.6V5h2" fill="none" stroke="#9a9a9a" stroke-width="1.2"/></svg>10 months ago</p>
        </article>
        <article class="card">
          <div class="card-image" role="img" aria-label="Photo of an actress in pink holding a small dog" style="background:linear-gradient(135deg,#b7b08f,#e8a3b8 50%,#e0457f)"></div>
          <p class="card-label">America</p>
          <h3 class="card-title">Rhea Westbrook Says They’re ”Thinking” About Another Simply Golden Sequel</h3>
          <p class="card-meta"><svg width="9" height="9" viewBox="0 0 10 10"><circle cx="5" cy="5" r="4" fill="none" stroke="#9a9a9a" stroke-width="1.2"/><path d="M5 2.6V5h2" fill="none" stroke="#9a9a9a" stroke-width="1.2"/></svg>10 months ago</p>
        </article>
        <article class="card">
          <div class="card-image" role="img" aria-label="Photo of two siblings on a red carpet at a music awards event" style="background:linear-gradient(90deg,#d8d4d4,#2f3d5c 35%,#e6e2dc 70%,#d4cfcf)"></div>
          <p class="card-label">America</p>
          <h3 class="card-title">Darren and Juliet Hale Are Both Returning to Stepping With the Stars for Season 23</h3>
          <p class="card-meta"><svg width="9" height="9" viewBox="0 0 10 10"><circle cx="5" cy="5" r="4" fill="none" stroke="#9a9a9a" stroke-width="1.2"/><path d="M5 2.6V5h2" fill="none" stroke="#9a9a9a" stroke-width="1.2"/></svg>10 months ago</p>
        </article>
        <article class="card">
          <div class="card-image" role="img" aria-label="Photo of an actress in a blue jumpsuit against a mint backdrop" style="background:linear-gradient(90deg,#a9ddd3,#3b6fb8 50%,#a9ddd3)"></div>
          <p class="card-label">America</p>
          <h3 class="card-title">Shriek Sisters Season 2’s Bloody New Photos Are Here and We Have a Lot of Questions</h3>
          <p class="card-meta"><svg width="9" height="9" viewBox="0 0 10 10"><circle cx="5" cy="5" r="4" fill="none" stroke="#9a9a9a" stroke-width="1.2"/><path d="M5 2.6V5h2" fill="none" stroke="#9a9a9a" stroke-width="1.2"/></svg>10 months ago</p>
        </article>
        <article class="card">
          <div class="card-image" role="img" aria-label="Portrait photo of an actress against a dark background" style="background:linear-gradient(90deg,#0f0a08,#3a2219 55%,#120c0a)"></div>
          <p class="card-label">America</p>
          <h3 class="card-title">Sara Pellman in Talks to Join All-Female Harbor’s 8 Spinoff: Other Women We Could Picture Joining</h3>
          <p class="card-meta"><svg width="9" height="9" viewBox="0 0 10 10"><circle cx="5" cy="5" r="4" fill="none" stroke="#9a9a9a" stroke-width="1.2"/><path d="M5 2.6V5h2" fill="none" stroke="#9a9a9a" stroke-width="1.2"/></svg>10 months ago</p>
        </article>
      </div>
    </section>

    <section class="category">
      <header class="category-head">
        <h2 class="category-tab">Europe</h2>
        <span class="view-all">VIEW ALL</span>
      </header>
      <div class="card-grid">
        <article class="card">
          <div class="card-image" role="img" aria-label="Photo of an actress recording voice work in a studio" style="background:linear-gradient(90deg,#5a4a3e,#3d6aa8 45%,#e3b65c 75%,#6c6c6c)"></div>
          <p class="card-label">Europe</p>
          <h3 class="card-title">Alma Ortega and Hugo Elias Guest Star on Starcastle’s Elvira of Aven</h3>
          <p class="card-meta"><svg width="9" height="9" viewBox="0 0 10 10"><circle cx="5" cy="5" r="4" fill="none" stroke="#9a9a9a" stroke-width="1.2"/><path d="M5 2.6V5h2" fill="none" stroke="#9a9a9a" stroke-width="1.2"/></svg>10 months ago</p>
        </article>
        <article class="card">
          <div class="card-image" role="img" aria-label="Photo of a TV cast gathered around a table in an office" style="background:linear-gradient(180deg,#4d4a3d,#2a2722 60%,#5a4d3c)"></div>
          <p class="card-label">Europe</p>
          <h3 class="card-title">Crime Unit Could Replace Theo Gilmore With 2 New Characters</h3>
          <p class="card-meta"><svg width="9" height="9" viewBox="0 0 10 10"><circle cx="5" cy="5" r="4" fill="none" stroke="#9a9a9a" stroke-width="1.2"/><path d="M5 2.6V5h2" fill="none" stroke="#9a9a9a" stroke-width="1.2"/></svg>10 months ago</p>
        </article>
        <article class="card">
          <div class="card-image" role="img" aria-label="Collage of three actor stills from film remakes" style="background:linear-gradient(90deg,#2e2b28,#4a3f33 33%,#8a5a2a 40%,#c58a3a 55%,#3a3530 70%,#6a6862)">
            <svg class="gallery-badge" viewBox="0 0 48 48" aria-hidden="true">
              <circle cx="24" cy="24" r="22.5" fill="rgba(0,0,0,.15)" stroke="#fff" stroke-width="2"/>
              <rect x="16" y="19" width="16" height="12" rx="1.5" fill="#fff"/>
              <rect x="20" y="17" width="6" height="3" fill="#fff"/>
              <circle cx="24" cy="25" r="3.5" fill="#3a3530"/>
              <circle cx="24" cy="25" r="1.8" fill="#fff"/>
            </svg>
          </div>
          <p class="card-label">Europe</p>
          <h3 class="card-title">TV Remake Madness Continues: The Latest Adaptations in the Works and Why This Trend Isn’t Stopping</h3>
          <p class="card-meta"><svg width="9" height="9" viewBox="0 0 10 10"><circle cx="5" cy="5" r="4" fill="none" stroke="#9a9a9a" stroke-width="1.2"/><path d="M5 2.6V5h2" fill="none" stroke="#9a9a9a" stroke-width="1.2"/></svg>10 months ago</p>
        </article>
      </div>
    </section>
  </main>
</div>
</body>
</html>
```